Wordpress Website for a startup software company - Submit mock up of home page, how long it will take you and your price to complete the entire website.

I am looking for a website to be created using the menu and items listed in the attached file. I am providing you the logo and style guide to use in the files.
The company is called K8. The product is called Tavo. You will see logos for both in the files.
The site will be hosted on be lumsey.
There is no purchase processing. This is an informational site only. It is to provide an intro to our technology and inspire the viewer to contact us for a demo or to try it.

The sight will need to be set up for SEO and google analytics.

You will need to select or create any graphics or images for the site.
If you use Wordpress Template that has to be purchased, I will include a milestone for the cost to reimburse you right afrer the award. Be sure to indicate in your proposal the cost of the template. Also be sure your price includes the cost of that template.

I will be selecting the winner based on the mock you create using the provided items.
This product is purchased by CTO's and CDO's.
The target market is Hotels/Resorts, Travel Sites, Airlines, Casinos and Large Retailers.

IF YOU DO NOT USE THE COLOR PALLETE PROVIDED IN THE TAVO PDF- I WILL NOT CONSIDER YOUR SUBMISSION. SORRY

```html
<!DOCTYPE html>
<html lang="en">
<head>
<meta charset="utf-8">
<title>Tavo by K8 — Our Software</title>
<link href="https://fonts.googleapis.com/css2?family=Roboto:wght@400;500&family=Montserrat:wght@500;600&display=swap" rel="stylesheet">
<style>
  :root {
    --shirt-blue: #4d6079;
    --wall-grey: #9a98a8;
    --sweater-beige: #b7aeb3;
    --screen-light: #e4e3ea;
    --desk-dark: #5f5a70;
    --tint: rgba(96, 80, 140, 0.22);
    --accent: #7b58c6;
    --white: #ffffff;
    --nav-text: rgba(255, 255, 255, 0.82);
  }
  * { margin: 0; padding: 0; box-sizing: border-box; }
  html, body { width: 1200px; height: 597px; overflow: hidden; }
  body { font-family: "Roboto", sans-serif; background: var(--wall-grey); }

  .hero { position: relative; width: 1200px; height: 597px; overflow: hidden; }
  .hero-photo {
    position: absolute;
    inset: 0;
    background:
      radial-gradient(ellipse 260px 230px at 250px 260px, rgba(70, 92, 125, 0.85), transparent 70%),
      radial-gradient(ellipse 140px 200px at 140px 500px, rgba(55, 60, 85, 0.75), transparent 75%),
      radial-gradient(ellipse 230px 200px at 640px 440px, rgba(205, 195, 200, 0.8), transparent 70%),
      radial-gradient(ellipse 260px 280px at 1060px 330px, rgba(240, 240, 246, 0.85), transparent 70%),
      radial-gradient(ellipse 60px 60px at 1015px 100px, rgba(70, 70, 80, 0.7), transparent 80%),
      radial-gradient(ellipse 250px 50px at 380px 570px, rgba(190, 170, 165, 0.6), transparent 80%),
      linear-gradient(100deg, #7f8096 0%, #9593a5 45%, #c3c1cc 100%);
  }
  .hero-tint { position: absolute; inset: 0; background: var(--tint); }

  .brand {
    position: absolute;
    left: 30px;
    top: 42px;
    display: flex;
    align-items: center;
    gap: 6px;
    color: var(--white);
    font-family: "Montserrat", sans-serif;
    font-weight: 600;
    font-size: 15px;
    letter-spacing: 0.5px;
  }
  .brand-mark { width: 14px; height: 14px; border-radius: 50%; background: var(--white); }

  .main-nav a {
    position: absolute;
    top: 23px;
    color: var(--nav-text);
    text-decoration: none;
    font-family: "Montserrat", sans-serif;
    font-size: 7.5px;
    font-weight: 500;
    letter-spacing: 0.6px;
    line-height: 9px;
  }
  .main-nav .is-current { left: 805px; color: var(--white); }
  .main-nav .nav-about { left: 849px; }
  .main-nav .nav-product { left: 897px; }
  .main-nav .nav-solutions { left: 955px; }
  .main-nav .nav-blog { left: 1017px; }
  .main-nav .demo-button {
    left: 1061px;
    top: 17px;
    width: 106px;
    height: 21px;
    line-height: 21px;
    text-align: center;
    background: var(--accent);
    color: var(--white);
    font-size: 8.5px;
    border-radius: 11px;
    letter-spacing: 0.7px;
  }

  .hero-title {
    position: absolute;
    left: 413px;
    width: 400px;
    top: 240px;
    text-align: center;
    color: var(--white);
    font-size: 48px;
    font-weight: 500;
    line-height: 56px;
  }
  .hero-lead {
    position: absolute;
    left: 363px;
    width: 500px;
    top: 306px;
    text-align: center;
    color: var(--white);
    font-size: 9.5px;
    letter-spacing: 1px;
  }
  .video-button {
    position: absolute;
    left: 557px;
    top: 335px;
    width: 112px;
    height: 21px;
    display: flex;
    align-items: center;
    justify-content: center;
    gap: 6px;
    background: var(--accent);
    color: var(--white);
    text-decoration: none;
    font-size: 8.5px;
    letter-spacing: 0.8px;
    border-radius: 11px;
  }
</style>
</head>
<body>
  <section class="hero">
    <div class="hero-photo" role="img" aria-label="Photo of a man in a plaid shirt and a woman in a knit hat working together at a computer in a bright office"></div>
    <div class="hero-tint"></div>

    <div class="brand"><span class="brand-mark"></span>TAVO by K8</div>

    <nav class="main-nav">
      <a href="#" class="is-current">HOME</a>
      <a href="#" class="nav-about">ABOUT</a>
      <a href="#" class="nav-product">PRODUCT</a>
      <a href="#" class="nav-solutions">SOLUTIONS</a>
      <a href="#" class="nav-blog">BLOG</a>
      <a href="#" class="demo-button">REQUEST A DEMO</a>
    </nav>

    <h1 class="hero-title">Our Software</h1>
    <p class="hero-lead">FOLLOW THE LINK BELOW FOR A QUICK VIDEO INTRODUCTION</p>
    <a href="#" class="video-button">
      <svg width="7" height="8" viewBox="0 0 6 7"><path d="M0 0 L6 3.5 L0 7 Z" fill="#ffffff"/></svg>
      VIEW OUR WORK
    </a>
  </section>
</body>
</html>
```